To design the Curriculum Vitae of a General Manager Legal

the objective is to redesign the attached Résumé for a senior level Internal Legal Executive in order to make it attractive, easily readable, catchy, modern looking while staying classy, elegant, sobre, and serious.
The résumé is attached to this project. it contains the followings sections : Photo; Contact Details; Summary; Education; Experience; Other.
Feel free to use photoshop to improve photo.
Updates

Target Market(s)

Legal community; law firms; Big corporations requiring internal legal senior executive

Font styles to use
Serif

Colors
ffffff
85cae6
33a6d7
0292cd
86cfc6
cfeae6
757575
919191
d9d9d9

Requirements
Must have
• classy; serious; professional; elegant; easy to read; catchy; modern;

```html
<!DOCTYPE html>
<html lang="en">
<head>
<meta charset="utf-8">
<title>Curriculum Vitae – Lina Haddad El Khoury</title>
<link href="https://fonts.googleapis.com/css2?family=Lato:wght@400;700&display=swap" rel="stylesheet">
<style>
:root{
  --blue:#0292cd;
  --blue-mid:#33a6d7;
  --ink:#333;
  --grey:#757575;
  --grey-light:#919191;
  --board:#e6e6e6;
  --white:#fff;
}
*{margin:0;padding:0;box-sizing:border-box}
html,body{width:800px;height:1200px;overflow:hidden}
body{background:var(--board);font-family:'Lato',sans-serif;color:var(--ink);position:relative}
.page{position:absolute;width:366px;height:518px;background:var(--white);box-shadow:0 1px 4px rgba(0,0,0,.28);overflow:hidden}
.page--one{left:14px;top:16px}
.page--two{left:417px;top:16px}
.page--three{left:216px;top:614px}
.page-label{position:absolute;font-size:20px;color:#555;letter-spacing:.5px}
.abs{position:absolute}

/* sidebar */
.sidebar{position:absolute;left:0;top:0;width:158px;height:100%;background:var(--blue);color:var(--white)}
.portrait{position:absolute;left:46px;top:18px;width:72px;height:72px;border-radius:50%;border:2px solid var(--white);background:radial-gradient(circle at 50% 40%,#b08a74,#5a3f33)}
.side-rail{position:absolute;left:19px;top:122px;width:1px;height:390px;background:rgba(255,255,255,.8)}
.side-list{position:absolute;left:25px;width:128px;font-size:5.2px;font-weight:700;line-height:1.35}
.side-list li{list-style:none;position:relative;margin-bottom:6px}
.side-list li::before{content:"";position:absolute;left:-8px;top:1px;width:4px;height:4px;border:1px solid #fff;border-radius:50%;background:var(--blue)}
.side-list .sub{font-weight:400;font-size:3.8px;margin:2px 0 0 2px}
.side-heading{position:absolute;left:0;width:158px;text-align:center;font-size:7px;text-decoration:underline;letter-spacing:.3px}
.side-icon{position:absolute;left:70px;width:17px;height:17px}
.side-job{margin-left:4px;font-size:4.8px}
.side-text{font-weight:400;font-size:3.8px;margin:3px 0 0 4px;text-align:justify}
.u{text-decoration:underline}

/* main column page 1 */
.name{position:absolute;left:179px;top:42px;font-size:12.5px;font-weight:700;letter-spacing:-.2px;color:#222}
.name span{font-weight:400}
.contact{position:absolute;left:179px;top:62px;font-size:5.2px;display:flex;gap:14px}
.contact svg{width:5px;height:5px;vertical-align:-1px;margin-right:2px}
.bracket{position:absolute;border-color:var(--blue);border-style:solid;border-width:0}
.h-sec{font-size:7px;color:var(--blue);font-weight:400;letter-spacing:.3px}
.body-text{font-size:3.9px;line-height:1.55;text-align:justify;color:#444}
.body-text p{margin-bottom:7px}
.sub-h{font-size:4.4px;text-decoration:underline;font-weight:700;color:#333;margin:4px 0 3px}
.bullets{list-style:none}
.bullets li{position:relative;padding-left:5px;font-size:3.8px;line-height:1.5;color:#444;margin-bottom:2px;text-align:justify}
.bullets li::before{content:"";position:absolute;left:0;top:2px;width:1.8px;height:1.8px;border-radius:50%;background:#555}

/* experience pages */
.date{font-size:5.6px;color:var(--blue);font-weight:700;margin-bottom:6px}
.role{font-size:5px;color:var(--blue-mid);margin:0 0 6px 5px}
.entry{margin-bottom:18px}
.entry .bullets{margin-left:2px}
</style>
</head>
<body>

<!-- PAGE 1 -->
<section class="page page--one">
  <aside class="sidebar">
    <div class="portrait" role="img" aria-label="Portrait photograph of the candidate"></div>
    <div class="side-rail"></div>
    <ul class="side-list" style="top:122px">
      <li>Nationalities : French - Syrian</li>
      <li>Married, 3 children</li>
      <li>Languages : Arabic, English, French.</li>
      <li>Member of the Franco-Gulf Business Forum and the Riviera Social Circle.</li>
      <li>Member in various NGO's and association working towards Women Empowerment and education of children refugee.</li>
    </ul>
    <svg class="side-icon" style="top:213px" viewBox="0 0 20 20"><circle cx="10" cy="10" r="10" fill="#fff"/><path d="M3 8l7-3 7 3-7 3z" fill="#0292cd"/><path d="M6 10v3c2 2 6 2 8 0v-3l-4 2z" fill="#0292cd"/></svg>
    <div class="side-heading" style="top:235px">EDUCATION</div>
    <ul class="side-list" style="top:252px">
      <li>Université Lumière Droit (Paris) Paris – France
        <div class="sub">• Master degree in Litigation, Arbitration, and Alternative Dispute Resolution (98-99)</div>
        <div class="sub">• Master degree in commercial law (97-98)</div>
      </li>
      <li>Institute of Legal Studies Paris - France (97-98)</li>
      <li>Levant State University – Syria
        <div class="sub">• Law degree (92-96)</div>
      </li>
    </ul>
    <svg class="side-icon" style="top:333px" viewBox="0 0 20 20"><circle cx="10" cy="10" r="10" fill="#fff"/><rect x="4" y="7" width="12" height="8" rx="1" fill="#0292cd"/><rect x="8" y="5" width="4" height="3" fill="none" stroke="#0292cd" stroke-width="1"/></svg>
    <div class="side-heading" style="top:355px">EXPERIENCE</div>
    <ul class="side-list" style="top:373px">
      <li>April 2017 - Present
        <div class="side-job" style="margin-top:4px">Legal Counsel at Qasr Al Noor Properties LLC ("QANP") -Dubai</div>
      </li>
      <li style="margin-top:8px">May 2015 - April 2017
        <div class="side-job" style="margin-top:4px">Senior Legal Counsel at Qasr Al Noor Retail Dayma Stores</div>
        <div class="side-text"><span class="u">Description of Position</span><br>Lead and manage the legal, compliance, functions and risk management function for QANP operations in Syria, Lebanon, Jordan, Iraq, Egypt, Georgia, Armenia &amp; Pakistan ("Countries"). A Legal Business Partner to drive business development agenda (organically, M&amp;A, digital/ecommerce), and contribute to functional strategies.</div>
        <div class="side-text u" style="margin-top:6px">Key Responsibilities</div>
      </li>
    </ul>
  </aside>

  <h1 class="name">LINA <span>HADDAD EL KHOURY</span></h1>
  <div class="contact">
    <span><svg viewBox="0 0 10 10"><circle cx="5" cy="5" r="5" fill="#222"/><path d="M3 2.5l1 .2.5 1.3-.6.5c.3.8.8 1.3 1.6 1.6l.5-.6 1.3.5.2 1c-2.5.6-5-2-4.5-4.5z" fill="#fff"/></svg>+971 50 5550123</span>
    <span><svg viewBox="0 0 10 10"><circle cx="5" cy="5" r="5" fill="#222"/><rect x="2.3" y="3.2" width="5.4" height="3.6" fill="#fff"/><path d="M2.3 3.2L5 5.3l2.7-2.1" fill="none" stroke="#222" stroke-width=".6"/></svg>lina.haddad@mailbox.com</span>
  </div>

  <div class="bracket" style="left:178px;top:94px;width:20px;height:192px;border-left-width:1px;border-top-width:1px"></div>
  <div class="abs" style="left:198px;top:90px;width:150px">
    <h2 class="h-sec" style="margin-bottom:8px">SUMMARY</h2>
  </div>
  <div class="abs body-text" style="left:188px;top:104px;width:160px">
    <p>A senior qualified legal professional with more than 15 years of experience in private practice and in-house focusing on the following industries: Real Estate, Retail and Services, obtained in UAE, France and Syria. Practice transactional skills (M&amp;A, real estate, commercial, corporate restructuring, strategic funding), organizational skills (policies and procedures and authority matrix covering different contexts in corporate environment), lawyering skills (preemptive legal advice, and a multi jurisdiction litigation management expertise), managerial skills (enhancing the value add of the legal department as both a service provider and a risk gatekeeper).</p>
    <p>Joined Qasr Al Noor Group in November 2011, an internationally recognized industry leader in shopping malls, communities, retail and leisure across the Middle East, Africa and Asia, first as Legal Counsel at Qasr Al Noor Properties responsible for UAE Shopping Malls, Project management and communities, and then moved in Mai 2015 to Qasr Al Noor Retail -Dayma Stores where currently I occupy the role of GM-Legal, focusing mainly on leading and managing the legal, compliance and risk management functions across a wide geographic area of countries.</p>
    <p>Prior to moving to Dubai, I have lived in Paris France, where I have worked in various organizations including the Global Chamber Court of Arbitration, a billing software company and a consultancy practice. I graduated from Université Lumière Droit Paris with two Master Degrees.</p>
    <p>Mother of Three, I am passionate about charitable work towards Women Empowerment and Refugee Children Education.</p>
  </div>

  <div class="bracket" style="left:188px;top:330px;width:20px;height:170px;border-left-width:1px;border-top-width:1px"></div>
  <div class="abs" style="left:196px;top:333px;width:154px">
    <div class="sub-h">Legal Division Leadership</div>
    <ul class="bullets">
      <li>Develop and execute the legal strategy and plans in alignment with strategic objectives of the company.</li>
      <li>Lead the Legal team across the Countries: attract, develop, assess and engage the right legal talents.</li>
      <li>Coordinating with management and Head of business units, evaluating strategy and merits and progress of specific projects.</li>
      <li>Manage and coordinate the Company's approach towards litigation to ensure cost effectiveness including negotiations of contracts with outside legal firms, monitor quality of work and delivery.</li>
    </ul>
    <div class="sub-h">M &amp; A</div>
    <ul class="bullets"><li>Contribute to M&amp;A and prospective acquisitions activities, perform due diligence, terms negotiations, closing and post-closing tasks.</li></ul>
    <div class="sub-h">Business Development / Partnership</div>
    <ul class="bullets">
      <li>Lead &amp; implement the legal expansion plans in Countries including setting up new legal entities, due diligence, and risk matrix.</li>
      <li>Prepare and structure complex contract negotiations. Examine intricate agreements and other documents for accuracy, legality and conformity with business standards.</li>
      <li>Oversee the legal process Prepare and review agreements, contracts regarding commercial development and business transactions: Memoranda of Understanding, Agreements to Lease and Lease Agreements, JVs, Franchise Agreements, Consultancy Agreements, Tender Documentation, Procurement Agreements, Mergers and Acquisitions, and other related to the development of company's business in the Countries.</li>
    </ul>
  </div>
</section>
<div class="page-label" style="left:166px;top:548px">PAGE 1</div>

<!-- PAGE 2 -->
<section class="page page--two">
  <div class="bracket" style="left:8px;top:8px;width:82px;height:95px;border-left-width:2px;border-top-width:2px"></div>
  <div class="bracket" style="left:238px;top:424px;width:119px;height:86px;border-right-width:2px;border-bottom-width:2px"></div>
  <div class="abs" style="left:25px;top:16px;width:330px">
    <div class="sub-h" style="margin-top:0">Digital</div>
    <ul class="bullets"><li>Perform all the legal aspects of QANP digital and ecommerce projects.</li></ul>
    <div class="sub-h">Corporate Governance &amp; Compliance</div>
    <ul class="bullets">
      <li>Create and secure protection of Intellectual property.</li>
      <li>Ensure the application of QANP corporate policies.</li>
      <li>Collaborate with the tax and finance groups to determine appropriate corporate structure.</li>
      <li>Communicate latest regulatory requirements to Business Units.</li>
      <li>Develop and maintain legal processes and business transactions compliance and related training; Provide support for governmental relations and regulatory affairs activities.</li>
    </ul>
    <div class="sub-h">Risk Management</div>
    <ul class="bullets">
      <li>Lead the implementation of risk control measures, contractual obligations and the structuring of transactions.</li>
      <li>Pragmatically, manage legal risks and providing alternative solutions to minimize liability exposure while achieving business goals.</li>
    </ul>
    <div class="sub-h">Others</div>
    <ul class="bullets">
      <li>Review and negotiate (in conjunction with the Treasury department) of financial documentation required to satisfy the funding, banking and other monetary services' requirements of the company.</li>
      <li>For new jurisdictions: Carry out legal research, due diligence procedures, prepare corporate documents and other formalities for the relevant operating companies. Establish methods to accomplish business goals whilst minimizing legal and commercial risks.</li>
      <li>Prepare board papers and updates to senior management.</li>
    </ul>
  </div>
  <div class="abs" style="left:22px;top:190px;width:1px;height:290px;background:var(--blue)"></div>
  <div class="abs" style="left:25px;top:191px;width:330px">
    <div class="entry">
      <div class="date">Nov 2011 - May 2015</div>
      <div class="role">Legal Counsel at Qasr Al Noor Properties LLC ("QANP") -Dubai</div>
      <div style="margin-left:5px">
        <div class="sub-h" style="margin-top:0">Description of Position</div>
        <div class="body-text" style="margin-bottom:3px">Lead and manage the Legal function related to the UAE shopping malls of QANP in Dubai, Ajman, Sharjah, and Fujairah (Development, JVs, land acquisitions, asset management, leasing construction and project management).</div>
        <div class="sub-h">Key Responsibilities</div>
        <ul class="bullets">
          <li>Prepared and reviews all the contracts related to the malls operation and asset management, including but not limited to leasing, procurement, operation, marketing, construction, development, consultancy, IT and HR.</li>
          <li>Provided legal advises and legal opinions on matters pertaining to the business of QANP and compliance with UAE laws.</li>
          <li>Handled the malls litigation cases, sending out legal notices, filing cases and preparing memos, preparing settlement agreements, referring disputes to external lawyers when necessary, managing and following up with the lawyers until complete execution of judgements.</li>
          <li>Negotiated with outside parties along with relevant internal clients for concluding commercial deals relating to the malls and preparing the required legal documents accordingly.</li>
          <li>Attending to the relevant local authority to obtain information or updates where required and to lobby or submit requests relating to the business requirements of QANP.</li>
          <li>Prepared various agreements related to business development of QANP in the UAE and the MENA Region (Joint Ventures, Sale and Purchase Agreements, Usufruct Agreements, Lease Agreements ...etc).</li>
          <li>Participated in negotiating and preparation of contracts related to development, design and construction of shopping malls in various countries in the MENA region (FIDIC, D&amp;B...etc).</li>
          <li>Participated in the preparation of legal documents and liaising with external lawyers in arbitration cases.</li>
          <li>Preparation of board papers and updates to senior management.</li>
          <li>Participated in the preparation of legal documentation and contracts relating to development, design, operation, selling of residences and management of a new real estate community in the Emirate of Sharjah.</li>
          <li>Provided internal training on adapting standard templates and legal documents.</li>
          <li>Participated in initiatives and prepared action plans to recognize and motivate performing employees of QANP, was chosen as culture champion for the legal department as part of a major culture change initiative undertaken by QANP.</li>
          <li>Coaching and supervising the work of the paralegal reporting to me ensuring that they perform their role efficiently and that they are able to grow and progress.</li>
        </ul>
      </div>
    </div>
    <div class="entry">
      <div class="date">Jan 2005 - June 2007</div>
      <div class="role">Orel Consulting Paris –France.</div>
      <div class="role">Responsible of legal and administrative affairs.</div>
      <ul class="bullets" style="margin-left:5px">
        <li>Prepared and revised the contracts and of the company</li>
        <li>Prepared the financial and legal statements of the company</li>
        <li>Insured that the company complied with French laws and regulation</li>
      </ul>
    </div>
  </div>
</section>
<div class="page-label" style="left:568px;top:548px">PAGE 2</div>

<!-- PAGE 3 -->
<section class="page page--three">
  <div class="bracket" style="left:8px;top:8px;width:120px;height:85px;border-left-width:2px;border-top-width:2px"></div>
  <div class="bracket" style="left:290px;top:425px;width:66px;height:85px;border-right-width:2px;border-bottom-width:2px"></div>
  <div class="abs" style="left:25px;top:22px;width:330px">
    <div class="entry">
      <div class="date">Jan 1999 - June 2002</div>
      <div class="role">Veridata SA</div>
      <div class="role">In house legal counsel at a software solution company Paris -France</div>
      <ul class="bullets">
        <li>Piloted the Legal and regulatory compliance aspects of transaction for the acquisition of the company by a German Fund and later on by a global leader in Outsourcing.</li>
        <li>Prepared and revised the contracts and legal documentations of the company.</li>
        <li>Insured that the company complied with French laws and regulation.</li>
      </ul>
    </div>
    <div class="entry">
      <div class="date">Mars-November 2000</div>
      <div class="role">Global Chamber Court of Arbitration Paris-France.</div>
      <div class="role">Assistant Counsel in the Secretariat of the</div>
      <ul class="bullets">
        <li>Counselled and drafted correspondence concerning all aspects of the Court Rules of arbitration.</li>
        <li>Prepared the agenda's to be presented to the Court on arbitration cases.</li>
        <li>Summarised and analysed draft awards before scrutiny by the Court.</li>
      </ul>
    </div>
    <div class="entry">
      <div class="date">February-April, 1999</div>
      <div class="role">Hartwell &amp; Marsh, Paris – France</div>
      <div class="role">Trainee at the Law firm</div>
      <ul class="bullets">
        <li>Prepared files in arbitration cases.</li>
        <li>Organised hearings in an international commercial arbitration.</li>
        <li>Researched work in business law, international public law and</li>
        <li>International commercial arbitration.</li>
        <li>Audit ir role efficiently and that they are able to grow and progress.</li>
      </ul>
    </div>
    <div class="entry">
      <div class="date">Mai-September, 1997</div>
      <div class="role">Rawda Law, Damascus - Syria.</div>
      <div class="role">Trainee at the Law firm</div>
      <ul class="bullets">
        <li>Activities in the field of civil, commercial and criminal law.</li>
        <li>Drafted commercial contracts.</li>
        <li>Consulted foreign companies on local laws and investment opportunities.</li>
      </ul>
    </div>
    <div class="entry">
      <div class="date">June-September, 1995, 1996</div>
      <div class="role">Karim Nassar, Damascus – Syria</div>
      <div class="role">Trainee in the Law firm of Professor</div>
      <div class="role">Specialist in commercial law</div>
      <ul class="bullets">
        <li>Prepared files in the field of international commercial arbitration.</li>
        <li>Participated at consultations in the domain of commercial law.</li>
      </ul>
    </div>
  </div>
</section>
<div class="page-label" style="left:366px;top:1142px">PAGE 3</div>

</body>
</html>
```